IT solutions & services company requires stationary makeover

Looking for a consistent modern, professional design across our printed client touch points:
Business Cards
Letterhead
Client proposal
Flyer
Postcard

We provide solutions for SME IT - servers, backups, AV etc, and the ongoing services around them.
we are happy with our logo - please see attached and would like the colour theme to be maintained.

```html
<!DOCTYPE html>
<html lang="en">
<head>
<meta charset="utf-8">
<title>Norvale – Business Card</title>
<link rel="stylesheet" href="https://fonts.googleapis.com/css2?family=Arimo:wght@400;700&display=swap">
<style>
  :root {
    --page-bg: #ece9e4;
    --card-bg: #ffffff;
    --ink-dark: #2b2b2b;
    --ink-grey: #6b6b6b;
    --brand-teal: #1b7a9a;
    --brand-sky: #6cc3e0;
    --brand-navy: #1f4d7a;
    --card-shadow: rgba(0, 0, 0, 0.18);
  }
  * { box-sizing: border-box; margin: 0; padding: 0; }
  html, body {
    width: 1200px;
    height: 801px;
    overflow: hidden;
  }
  body {
    background: var(--page-bg);
    font-family: "Arimo", Arial, sans-serif;
    display: flex;
    align-items: center;
    justify-content: center;
    gap: 60px;
  }
  .card {
    position: relative;
    width: 480px;
    height: 274px;
    background: var(--card-bg);
    box-shadow: 0 6px 18px var(--card-shadow);
  }

  /* Front of card */
  .card-front .brand {
    position: absolute;
    left: 46px;
    top: 108px;
  }
  .card-front .brand-name {
    font-size: 40px;
    font-weight: 400;
    color: var(--ink-dark);
    letter-spacing: 0.5px;
  }
  .card-front .tagline {
    margin-top: 6px;
    font-size: 9px;
    letter-spacing: 1px;
    text-transform: uppercase;
    color: var(--ink-grey);
  }
  .card-front .brand-dot {
    position: absolute;
    right: 44px;
    top: 62px;
    width: 150px;
    height: 150px;
  }

  /* Back of card */
  .card-back .holder {
    position: absolute;
    left: 30px;
    top: 26px;
  }
  .card-back .holder-name {
    font-size: 22px;
    color: var(--brand-navy);
  }
  .card-back .holder-role {
    font-size: 11px;
    color: var(--ink-grey);
  }
  .card-back .contact {
    position: absolute;
    left: 30px;
    top: 118px;
    font-size: 11px;
    line-height: 1.45;
    color: var(--ink-grey);
    list-style: none;
  }
  .card-back .contact .web {
    font-weight: 700;
    color: var(--brand-navy);
    margin-top: 2px;
  }
  .card-back .brand-dot {
    position: absolute;
    right: 40px;
    top: 86px;
    width: 130px;
    height: 130px;
  }
</style>
</head>
<body>

  <section class="card card-front" aria-label="Business card front">
    <div class="brand">
      <div class="brand-name">Norvale</div>
      <div class="tagline">Your solution partner</div>
    </div>
    <svg class="brand-dot" viewBox="0 0 150 150" aria-hidden="true">
      <circle cx="75" cy="75" r="62" fill="var(--brand-teal)"/>
    </svg>
  </section>

  <section class="card card-back" aria-label="Business card back">
    <div class="holder">
      <div class="holder-name">Marcus Hale</div>
      <div class="holder-role">chief executive officer</div>
    </div>
    <ul class="contact">
      <li>03 555 0182</li>
      <li>mhale@norvale.co.nz</li>
      <li>Level 2,</li>
      <li>Ashgrove Lane,</li>
      <li>Hillcrest, NZ</li>
      <li class="web">www.norvale.co.nz</li>
    </ul>
    <svg class="brand-dot" viewBox="0 0 130 130" aria-hidden="true">
      <circle cx="65" cy="65" r="52" fill="var(--brand-sky)"/>
    </svg>
  </section>

</body>
</html>
```